dealcraftmentor.com - Podcast Guest Marketing E-Flyer PDF

Dear Designers:I am in need of an attractive and attention-getting layout and design for a three-page marketing flyer (commonly known as a media one sheet) that will be sent via e-mail, as PDF file, to various Podcast hosts to market me as a guest on their podcasts. I want the design of the document to "mirror" the design and branding on my parent dealcraftmentor.com website. I am providing ALL the edited and proofread copy and content - the designer just needs to create the design for this marketing document. I want an active PDF document and icons should be used for WorkLoop, Phone, E-mail , and website- with hyperlinks that connect accordingly. I need a fast turnaround.
Updates

Dear Designers - instead of using the photo in the project file of me speaking to the audience for the banner image - I thought it would be a better idea to make this marketing piece specific to Podcast Hosts. Therefore, an image such as the one in the link below would be good to use for a banner image. https://www.pixelvarnow.com/find?q=podcast+studio+photos&mode=img&ref=univ&id=Qm7TzRk2LwPa9XcNvB4eHyU8sDjF1gA5oE3iKtZ6bW0nMh&w=1377&h=804#pic=vrolapemxq3BcT:

Target Market(s)

This PDF document will be sent to 650 Podcast hosts in North America via a broadcast e-mail.

Font styles to use
Sans Serif

Colors
ec1f27
ffffff
000000
333333
9d9d9d

Requirements
Must have
• A three-page layout that is easy to navigate in PDF form.
• Proper font styles and sizes for key emphasis areas on the document/
• Consistent branding to mirror my dealcraftmentor.com parent website
• Must be easy for people to read
• Attention-getting design elements and layout
• Professional and sophisticated design
• Icons for contact information
Should not have
• Should not be cluttered and junky-looking.
• Should not use small font sizes that makes it difficult to read.
• If Podcast hosts are interested in having me as a guest - they will read the content as required on three-pages

```html
<!DOCTYPE html>
<html lang="en">
<head>
<meta charset="utf-8">
<title>dealcraftmentor.com – Podcast Guest One Sheet</title>
<link rel="stylesheet" href="https://fonts.googleapis.com/css2?family=Montserrat:wght@500;600;700;800&family=Open+Sans:ital,wght@0,400;0,600;0,700;1,400;1,600&display=swap">
<style>
:root{
  --red:#ec1f27;
  --red-dark:#a5141a;
  --black:#000000;
  --ink:#333333;
  --grey:#9d9d9d;
  --panel:#e6e6e6;
  --white:#ffffff;
  --board:#b7b7b7;
}
*{box-sizing:border-box;margin:0;padding:0}
html,body{width:897px;height:1200px;overflow:hidden}
body{background:var(--board);font-family:"Open Sans",Arial,sans-serif;color:var(--ink);position:relative}
.page{position:absolute;top:182px;width:247px;height:351px;background:var(--white);overflow:hidden;box-shadow:0 2px 6px rgba(0,0,0,.25)}
.page--media{left:61px}
.page--intro{left:327px}
.page--contact{left:590px;background:linear-gradient(135deg,#ffffff 0%,#eeeeee 45%,#f7f7f7 60%,#e9e9e9 100%)}

.brand{display:flex;align-items:center;gap:3px;font-family:"Montserrat",sans-serif;font-weight:600;color:var(--ink)}
.brand__mark{width:8px;height:8px;background:var(--red)}
.brand__name{font-size:6.4px;letter-spacing:-.1px}

.pill{background:#2b2b2b;color:var(--white);font-family:"Montserrat",sans-serif;font-weight:700;font-size:3.1px;text-align:center;border-radius:6px;padding:2.6px 4px;box-shadow:0 1px 0 var(--red);white-space:nowrap;overflow:hidden}
.copy{font-size:2.75px;line-height:1.42}
.copy p+p{margin-top:2px}

.foot{position:absolute;left:0;bottom:0;width:100%;height:15px;background:var(--red)}
.foot svg.black{position:absolute;right:0;top:0}
.foot__item{position:absolute;top:5px;font-family:"Montserrat",sans-serif;font-weight:600;font-size:3.1px;color:var(--white);display:flex;align-items:center;gap:1.5px;white-space:nowrap}
.foot__item i{display:inline-block;width:3px;height:2.4px;background:var(--white)}
.foot__web{right:14px}

/* page 1 */
.media-head{position:absolute;left:0;top:0;width:100%;height:74px;background:linear-gradient(180deg,#b3161d 0%,var(--red-dark) 60%,#8e1117 100%)}
.media-head svg{position:absolute;left:0;top:0}
.media-head .brand{position:absolute;left:10px;top:14px}
.media-head__text{position:absolute;right:14px;top:27px;width:200px;text-align:right;color:var(--white)}
.media-head__title{font-family:"Montserrat",sans-serif;font-weight:700;font-size:3.8px}
.media-head__lead{font-family:"Montserrat",sans-serif;font-weight:600;font-size:3.2px;margin-top:2px;line-height:1.35}
.media-head__outlets{font-style:italic;font-weight:600;font-size:2.6px;margin-top:4px;line-height:1.4}
.profit{position:absolute;left:14px;right:14px;top:78px;height:76px;background:var(--panel);border-radius:8px}
.profit .pill{position:absolute;left:2px;right:2px;top:2px}
.profit__body{position:absolute;left:14px;right:14px;top:16px}
.profit__intro{font-family:"Montserrat",sans-serif;font-weight:700;font-size:2.8px;text-align:center;margin-bottom:3px;line-height:1.35}
.note{position:absolute;left:0;right:0;top:160px;text-align:center;font-weight:700;font-style:italic;font-size:2.8px}
.testi-pill{position:absolute;left:46px;right:46px;top:169px}
.quote{position:absolute;left:38px;right:38px;border:0.8px solid var(--grey);border-radius:8px;background:var(--white);padding:5px 6px 3px}
.quote::before{content:"\201C";position:absolute;left:2px;top:-3px;font-family:Georgia,serif;font-weight:700;font-size:8px;color:var(--ink)}
.quote--host{top:187px;height:46px}
.quote--event{top:251px;height:55px}
.quote .copy{font-style:italic;font-size:2.45px}
.quote__by{text-align:right;margin-top:2px;font-size:2.2px}
.quote__by b{color:var(--red);font-style:italic}
.event-intro{position:absolute;left:40px;right:40px;top:237px;text-align:center;font-weight:700;font-size:2.8px;line-height:1.35}
.event-by{position:absolute;right:54px;top:309px;width:90px;text-align:right;font-weight:700;font-size:2.45px;line-height:1.3}

/* page 2 */
.intro-band{position:absolute;top:0;right:0}
.intro-band__label{position:absolute;right:10px;top:7px;font-family:"Montserrat",sans-serif;font-weight:700;font-size:3.3px;color:var(--white);white-space:nowrap}
.intro-banner{position:absolute;left:0;top:20px;width:100%;height:92px;background:linear-gradient(100deg,#1a1a1a 0%,#3a3a3a 45%,#6d6d6d 70%,#2c2c2c 100%)}
.intro-logo-tab{position:absolute;left:0;top:0}
.page--intro .brand{position:absolute;left:10px;top:14px}
.intro-banner__text{position:absolute;left:10px;top:52px;width:126px;color:var(--white)}
.intro-banner__kicker{font-family:"Montserrat",sans-serif;font-weight:700;font-size:3.2px;white-space:nowrap}
.intro-banner__title{font-family:"Montserrat",sans-serif;font-weight:700;font-size:6.6px;line-height:1.1;color:var(--red);margin-top:2px}
.intro-banner__lead{font-size:2.6px;line-height:1.4;margin-top:2px}
.why-pill{position:absolute;left:44px;right:44px;top:107px}
.why-copy{position:absolute;left:16px;right:16px;top:123px;text-align:center}
.six-pill{position:absolute;left:48px;right:48px;top:157px}
.reasons{position:absolute;left:14px;right:14px;top:174px;display:grid;grid-template-columns:1fr 1fr;column-gap:12px}
.reason{position:relative;padding-left:7px;margin-bottom:4px;font-size:2.5px;line-height:1.42;text-align:justify}
.reason::before{content:"";position:absolute;left:0;top:.6px;width:3.6px;height:3.6px;border-radius:50%;background:var(--red)}
.benefit{position:absolute;left:14px;right:14px;top:266px;height:66px;background:var(--panel);border-radius:8px 8px 0 0}
.benefit .pill{position:absolute;left:2px;right:2px;top:2px}
.benefit .copy{position:absolute;left:12px;right:12px;top:15px;text-align:center;font-size:2.5px}

/* page 3 */
.cover-texture{position:absolute;inset:0;background:linear-gradient(150deg,rgba(255,255,255,0) 0%,rgba(255,255,255,.8) 30%,rgba(220,220,220,.4) 55%,rgba(255,255,255,.7) 80%)}
.cover-brand{position:absolute;left:0;right:0;top:174px;justify-content:center;gap:5px}
.cover-brand .brand__mark{width:18px;height:18px}
.cover-brand .brand__name{font-size:14px}
.card{position:absolute;left:50px;top:214px;width:164px;height:52px;background:var(--white);border-radius:12px;box-shadow:0 1px 4px rgba(0,0,0,.18)}
.headshot{position:absolute;left:34px;top:220px;width:38px;height:38px;border-radius:50%;background:radial-gradient(circle at 50% 40%,#8a8a8a 0%,#4a4a4a 60%,#2a2a2a 100%);border:2px solid var(--white);box-shadow:0 1px 4px rgba(0,0,0,.3)}
.contacts{position:absolute;left:86px;top:223px;list-style:none;font-family:"Montserrat",sans-serif;font-weight:600;font-size:4.2px;color:var(--ink)}
.contacts li{display:flex;align-items:center;gap:3px;margin-bottom:3.4px;white-space:nowrap}
.contacts svg{flex:none}
</style>
</head>
<body>

<section class="page page--media">
  <header class="media-head">
    <svg width="247" height="74" viewBox="0 0 247 74">
      <polygon points="0,0 118,0 100,32 0,32" fill="#ffffff"/>
      <polygon points="100,32 118,0 130,0 110,36 0,36 0,32" fill="#d9d9d9" opacity=".5"/>
    </svg>
    <div class="brand"><span class="brand__mark"></span><span class="brand__name">dealcraftmentor</span></div>
    <div class="media-head__text">
      <p class="media-head__title">DANIEL R. WHITMORE IN THE MEDIA</p>
      <p class="media-head__lead">Daniel has appeared on radio programs, written articles or contributed to articles for the following media outlets:</p>
      <p class="media-head__outlets">Show Logos - Northern Ledger newspaper, Marketwise.com, Capitalview.com, Vantage Open Forum for Small Business, and Closing Edge and Margin magazines. Note to Graphic Artist - please use the current logos for the above referenced media outlets.</p>
    </div>
  </header>

  <div class="profit">
    <p class="pill">Three Ways You Can Profit From Booking Daniel R. Whitmore on Your Podcast</p>
    <div class="profit__body">
      <p class="profit__intro">Upon mutual agreement, podcast hosts and listeners can have access to the following money-saving and profit-generating opportunities:</p>
      <div class="copy">
        <p>1. Podcast hosts will be provided with a specific promotional code to share with your listeners that will entitle them to receive a special one-time discount of $19.95US off the purchase of the MP3 download of the Deal Ready Toolkit Audio Learning Program available on my online store. Complete download and purchase instructions will be provided to podcast hosts to publish in your notes and also communicate to your listeners.</p>
        <p>2. Podcast hosts will receive a 10% commission payable on the net sales dollar revenue generated from the sale of MP3 downloads of Daniel's Deal Ready Toolkit Audio Learning Program.</p>
        <p>3. Podcast hosts will receive a 10% referral fee for any corporation or association that books Daniel for a presentation, seminar, or learning workshop that directly results from my participation on your podcast.</p>
      </div>
    </div>
  </div>

  <p class="note">Note: Discount and commission payments are subject to agreement to standard terms and conditions.</p>
  <p class="pill testi-pill">Testimonials: What Some Clients Are Saying About the Deal Craft Mentor®</p>

  <blockquote class="quote quote--host">
    <p class="copy">Daniel Whitmore did a terrific job on my podcast. His negotiating insights and tips were well received by my listeners and he was an engaging, knowledgeable, and entertaining guest. Given my expertise in real estate, I thought I was a good negotiator – until Daniel taught me a few new strategies and tips during the podcast. I would recommend Daniel to any podcast host – he is a pro and his topics are relevant and can benefit everyone.</p>
    <p class="quote__by"><b>Mark Ellison/ Podcast Host</b><br>Property Investor Roundtable Podcast, San Antonio, Texas</p>
  </blockquote>

  <p class="event-intro">Below is a partial listing of testimonials from attendees at a Founders' Circle (FC) event provided by the RT Calloway, Chapter Learning Chair:</p>

  <blockquote class="quote quote--event">
    <div class="copy">
      <p>“A very engaging, entertaining, and inspirational speaker who provided very useful information, strategies, and tips to apply to all my future negotiations.”</p>
      <p>“Thank you to FC Western New York for booking this speaker! I learned some things that I can address immediately and a lot of material that I need to practice. Great session!”</p>
      <p>“Daniel was an outstanding speaker on the topic of negotiating! He was one of my favorite speakers ever! Daniel was a real ‘teacher’ versus other typical speakers who spend two hours bragging or promoting their book.”</p>
      <p>“Daniel was a very knowledgeable and well-prepared speaker who provided helpful tips and scripts throughout the entire presentation! I would love to learn more from this speaker!”</p>
    </div>
  </blockquote>

  <p class="event-by">RT Calloway, CEO and President<br>Harborline Records Services<br>Founders' Circle (FC) Western New York<br>Learning Chair</p>

  <footer class="foot">
    <svg class="black" width="95" height="15" viewBox="0 0 95 15"><polygon points="10,0 95,0 95,15 0,15" fill="#000"/></svg>
    <span class="foot__item" style="left:10px"><i></i>E-mail: daniel@whitmoremail.com</span>
    <span class="foot__item" style="left:84px"><i></i>Phone: 555-014-2290</span>
    <span class="foot__item foot__web"><i style="border-radius:50%;width:2.6px;height:2.6px"></i>www.dealcraftmentor.com</span>
  </footer>
</section>

<section class="page page--intro">
  <div class="intro-banner" role="img" aria-label="Black and white banner photo of a podcast studio setting"></div>
  <svg class="intro-logo-tab" width="130" height="36" viewBox="0 0 130 36">
    <polygon points="0,0 116,0 98,34 0,34" fill="#ffffff"/>
  </svg>
  <svg class="intro-band" width="110" height="20" viewBox="0 0 110 20">
    <polygon points="10,0 110,0 110,20 0,20" fill="#ec1f27"/>
  </svg>
  <span class="intro-band__label">Daniel's Headshot, Banner Image, and Branding</span>
  <div class="brand"><span class="brand__mark"></span><span class="brand__name">dealcraftmentor</span></div>

  <div class="intro-banner__text">
    <p class="intro-banner__kicker">MEET DEAL CRAFT MENTOR® DANIEL R. WHITMORE</p>
    <h1 class="intro-banner__title">THE EXPERT YOU NEED AS<br>A GUEST ON YOUR PODCAST</h1>
    <p class="intro-banner__lead">Are you looking for a relevant and appealing topic and an engaging subject matter expert who can provide immeasurable value and life-changing tips to the listeners of your podcast?</p>
  </div>

  <p class="pill why-pill">Why Negotiating and Decision Making Should Be Topics on Your Podcast</p>
  <div class="copy why-copy">
    <p>Regardless of your podcast theme – it's important to remember that your listeners are negotiating all the time – in their personal lives, social lives, and especially in their business lives. Negotiating is an essential life skill. Everyone can improve his or her negotiating skills, and Daniel is the expert who can provide the answers your people crave.</p>
    <p>Your podcast listeners will benefit from Daniel's proven, practical, and relevant negotiating strategies and tips that will improve results and outcomes in all types of personal and business negotiations.</p>
  </div>

  <p class="pill six-pill">Six Reasons to Book Daniel R. Whitmore As a Guest on Your Podcast</p>
  <div class="reasons">
    <div>
      <p class="reason">Daniel is a dynamic, thought-provoking, engaging, captivating, and entertaining speaker who will share some great personal stories to help your listeners better understand and relate to the topic of negotiating and decision-making dynamics. He will indeed challenge the “status quo.”</p>
      <p class="reason">His five-star-rated presentations and training programs have been delivered around the world to small and medium-sized businesses, Top 500 ranked corporations, and large industry, trade, and peer-to-peer associations such as Rising Leaders' Council and Founders' Circle.</p>
      <p class="reason">With formal training in broadcasting and media arts, Daniel provides 30 years of experience as a professional speaker who can provide your listeners with valuable insights, solutions, and answers to address listeners' challenges and questions.</p>
    </div>
    <div>
      <p class="reason">Daniel is the founder of dealcraftmentor.com® and is an internationally recognized expert and highly rated speaker on the topics of negotiating and decision-making dynamics that affect negotiated outcomes. His versatility and commitment to proper preparation will ensure that his content is tailored to address the theme of your podcast and the needs of your listeners.</p>
      <p class="reason">Daniel has personally trained over 50,000 people of all experience levels across multiple industries, in 31 countries how to negotiate more effectively.</p>
      <p class="reason">Daniel is the creator of the best-selling Deal Ready Toolkit Audio Learning Program – designed to be an effective all-in-one learning solution that helps people improve their negotiating capabilities and skills. He is also the host of his soon-to-be-launched Podcast – Closing Table Talk.</p>
    </div>
  </div>

  <div class="benefit">
    <p class="pill">How Podcast Listeners Will Benefit</p>
    <div class="copy">
      <p>Most people are intimidated by the prospect and process of negotiating – and often view negotiating as an uncomfortable haggling and bargaining process that may involve confrontation, anxiety, and stress. If podcast listeners are like most people – then they probably are concerned about being taken advantage of – or that they are missing out on potential opportunities in their personal, social, and business negotiations.</p>
      <p>To alleviate your listeners' concerns, Daniel will provide them with easy-to-understand negotiating strategies, tactics, phrases, and tips they can immediately apply – the moment the podcast episode ends. Your listeners will feel more confident when they are equipped with the powerful and beneficial strategies and techniques that will help them save/make money and arrive at better outcomes when negotiating with customers, clients, suppliers, contractors, financial institutions, retailers, co-workers, colleagues, and family members.</p>
    </div>
  </div>

  <footer class="foot">
    <svg class="black" width="95" height="15" viewBox="0 0 95 15"><polygon points="10,0 95,0 95,15 0,15" fill="#000"/></svg>
    <span class="foot__item" style="left:10px"><i></i>E-mail: daniel@whitmoremail.com</span>
    <span class="foot__item" style="left:84px"><i></i>Phone: 555-014-2290</span>
    <span class="foot__item foot__web"><i style="border-radius:50%;width:2.6px;height:2.6px"></i>www.dealcraftmentor.com</span>
  </footer>
</section>

<section class="page page--contact">
  <div class="cover-texture" role="img" aria-label="Soft light grey diagonal texture background"></div>
  <div class="brand cover-brand"><span class="brand__mark"></span><span class="brand__name">dealcraftmentor</span></div>
  <div class="card"></div>
  <div class="headshot" role="img" aria-label="Circular headshot photo of Daniel R. Whitmore"></div>
  <ul class="contacts">
    <li><svg width="5" height="4" viewBox="0 0 10 8"><rect width="10" height="8" rx="1" fill="#ec1f27"/><polyline points="0.5,0.8 5,4.5 9.5,0.8" fill="none" stroke="#fff" stroke-width="1.2"/></svg>E-mail: daniel@whitmoremail.com</li>
    <li><svg width="5" height="5" viewBox="0 0 10 10"><rect width="10" height="10" rx="1.5" fill="#ec1f27"/><rect x="3.3" y="1.6" width="3.4" height="6.8" rx=".8" fill="#fff"/></svg>Phone: 555-014-2290</li>
    <li><svg width="5" height="5" viewBox="0 0 10 10"><rect width="10" height="10" rx="1.5" fill="#ec1f27"/><path d="M3 7 L7 3 M4.5 3 H7 V5.5" fill="none" stroke="#fff" stroke-width="1.3"/></svg>WorkLoop Profile: workloop.com/in/danielwhitmore</li>
    <li><svg width="5" height="5" viewBox="0 0 10 10"><circle cx="5" cy="5" r="5" fill="#ec1f27"/><circle cx="5" cy="5" r="2.8" fill="none" stroke="#fff" stroke-width="1"/><line x1="2.2" y1="5" x2="7.8" y2="5" stroke="#fff" stroke-width=".8"/></svg>Website: dealcraftmentor.com</li>
  </ul>
</section>

</body>
</html>
```